Infographic Table of AI Pricing Options for LinkedIn post

Turn this table (in the powerpoint slide attached) into an attractively formatted infographic table for Strelquin (www.strelquin.com).
This will be an infographic displayed on a linkedin post from a consultant from Strelquin.
Try to keep it on brand with Strelquin look and feel.

Target Market(s)

Tech and SaaS CEOs and Founders; Private Equity and Venture Capital employees

Industry/Entity Type

Management Consulting

Colors
0054AA
0677BA
7BADD7
CADEEF
E8F1F8

```html
<!DOCTYPE html>
<html lang="en">
<head>
<meta charset="utf-8">
<title>Challenges of GenAI Monetization – Strelquin</title>
<link rel="stylesheet" href="https://fonts.googleapis.com/css2?family=Outfit:wght@400;500;600;700;800&display=swap">
<style>
  :root{
    --navy-deep:#0d0f2e;
    --navy-mid:#1b2257;
    --navy-light:#2e3d82;
    --band:#263a6e;
    --teal:#3fc4c0;
    --sky:#4aa3e0;
    --card:#f7f8fb;
    --ink:#14162e;
    --rule:#8790b8;
    --pro:#1fb45a;
    --con:#e8141c;
    --white:#ffffff;
  }
  *{margin:0;padding:0;box-sizing:border-box}
  html,body{width:1200px;height:628px;overflow:hidden}
  body{
    font-family:"Outfit",sans-serif;
    background:linear-gradient(120deg,var(--navy-deep) 0%,var(--navy-mid) 55%,var(--navy-light) 100%);
    color:var(--white);
    position:relative;
  }
  .headline{
    position:absolute;left:24px;top:20px;width:1170px;
    font-size:40px;font-weight:400;line-height:50px;letter-spacing:-.9px;
  }
  .headline-line{display:block;white-space:nowrap}
  .headline strong{
    font-weight:700;letter-spacing:-1.1px;
    background:linear-gradient(90deg,var(--teal),var(--sky));
    -webkit-background-clip:text;background-clip:text;color:transparent;
  }
  .section-band{
    position:absolute;left:19px;top:137px;right:0;height:46px;
    background:linear-gradient(90deg,var(--band),rgba(38,58,110,.35));
    display:flex;align-items:center;
  }
  .section-band::before{
    content:"";position:absolute;left:0;top:0;bottom:0;width:17px;
    background:linear-gradient(180deg,var(--teal),var(--sky));
    border-radius:4px 0 0 4px;
  }
  .section-band h2{margin-left:36px;font-size:25px;font-weight:500}
  .card{
    position:absolute;left:19px;top:204px;width:1160px;height:440px;
    background:var(--card);border-radius:19px;color:var(--ink);
  }
  .tag{position:absolute;top:9px;font-size:11px;letter-spacing:1.6px;font-weight:500}
  .tag--today{left:123px}
  .tag--future{left:915px}
  .pricing-table{
    position:absolute;left:17px;top:29px;width:1127px;
    display:grid;grid-template-columns:100px 307px 271px 220px 229px;
  }
  .col-head{
    height:51px;display:flex;align-items:center;gap:10px;padding-left:12px;
    background:linear-gradient(90deg,var(--navy-deep),var(--navy-mid));
    color:var(--white);font-weight:800;font-size:18px;line-height:17px;letter-spacing:.3px;
  }
  .col-head:last-child{border-radius:0 10px 10px 0;background:linear-gradient(90deg,var(--navy-mid),var(--navy-light))}
  .head-blank{background:var(--white);border-radius:8px 0 0 8px}
  .letter{
    width:35px;height:35px;flex:none;display:grid;place-items:center;
    background:linear-gradient(135deg,var(--teal),var(--sky));
    color:var(--white);font-size:24px;font-weight:800;
  }
  .row-label{font-size:17px;padding-top:8px}
  .cell{border-left:1px solid var(--rule);padding:8px 6px 0 9px}
  .row-rule{grid-column:1/-1;height:1px;background:var(--rule);margin-left:16px;margin-right:19px}
  .row--desc{height:91px;padding-top:16px}
  .row--ex{height:53px}
  .row--pros{height:82px}
  .row--cons{height:110px}
  .desc{font-size:17px;line-height:21.5px}
  .examples{display:flex;align-items:center;gap:26px;padding-top:0}
  .brand{display:flex;align-items:center;gap:7px;font-size:18px;font-weight:600;color:var(--ink)}
  .brand i{width:28px;height:28px;background:var(--ink);border-radius:6px;display:block}
  .aside{font-style:italic;font-size:14px}
  .list{font-size:15px;line-height:21.5px}
  .list--big{font-size:18px;line-height:22px}
  .list--nowrap{white-space:nowrap;font-size:17px}
  .pro,.con{position:relative;padding-left:13px;display:inline}
  .pro::before,.con::before{content:"";position:absolute;left:0;top:7px;width:7px;height:7px;border-radius:50%}
  .pro::before{border:2px solid var(--pro)}
  .con::before{background:var(--con)}
  .stack .con,.stack .pro{display:block}
  .brand-tab{
    position:absolute;left:995px;top:559px;width:205px;height:69px;
    background:var(--navy-light);border-top-left-radius:18px;
  }
  .brand-pill{
    position:absolute;left:14px;top:13px;width:160px;height:41px;border-radius:12px;
    background:var(--white);display:flex;align-items:center;gap:8px;padding-left:14px;
    color:var(--navy-mid);font-size:23px;font-weight:500;
  }
  .brand-pill i{width:22px;height:22px;background:var(--sky);border-radius:4px;display:block}
</style>
</head>
<body>
  <h1 class="headline">
    <span class="headline-line">There are <strong>3 MAJOR MONETIZATION MODELS</strong> that have begun</span>
    <span class="headline-line">to gain traction with AI, and one we expect to see more of.</span>
  </h1>

  <div class="section-band"><h2>Challenges of GenAI Monetization</h2></div>

  <section class="card">
    <span class="tag tag--today">*FREQUENTLY SEEN TODAY</span>
    <span class="tag tag--future">*FUTURE OPTION?</span>

    <div class="pricing-table">
      <div class="head-blank"></div>
      <div class="col-head"><span class="letter">A</span>User licenses</div>
      <div class="col-head"><span class="letter">B</span>Usage-based<br>tokens</div>
      <div class="col-head"><span class="letter">C</span>Outcome-based</div>
      <div class="col-head"><span class="letter">D</span>Usage-tiered<br>licenses</div>

      <div class="row-label row--desc">Description</div>
      <div class="cell desc row--desc">Charge a flat price for a user to have access to the functionality</div>
      <div class="cell desc row--desc">Purchase blocks of tokens that can be spend on usage/work of the AI functionality</div>
      <div class="cell desc row--desc">Pay for the outcomes of the GenAI functionality</div>
      <div class="cell desc row--desc">Offer different user licenses with different usage capacities</div>
      <div class="row-rule"></div>

      <div class="row-label row--ex">Examples</div>
      <div class="cell examples row--ex"><span class="brand"><i></i>Chatwell</span><span class="brand"><i></i>Pilotra</span></div>
      <div class="cell examples"><span class="brand">Tokenly</span><span class="brand" style="font-size:13px">Visio Lens API</span></div>
      <div class="cell examples" style="gap:14px"><span class="brand" style="font-size:15px">Helpdeskr</span><span class="brand" style="font-size:15px">Paystream</span></div>
      <div class="cell examples" style="gap:18px"><span class="brand"><i></i>Chatwell</span><span class="aside">kinda...</span></div>
      <div class="row-rule"></div>

      <div class="row-label row--pros">Pros</div>
      <div class="cell list list--big row--pros"><span class="pro">Simple and easily understood</span></div>
      <div class="cell list"><span class="pro">Covers costs at all scales of usage Tokens help with predictability issues</span></div>
      <div class="cell list list--big"><span class="pro">Potentially highly value-aligned</span></div>
      <div class="cell list"><span class="pro">Value aligned</span> <span class="pro">Simple &amp; predictable</span> <span class="pro">Natural upsell path</span> <span class="pro">Low barrier to adoption</span></div>
      <div class="row-rule"></div>

      <div class="row-label row--cons">Cons</div>
      <div class="cell list row--cons"><span class="con">High price limits adoption</span> <span class="con">Not tightly value aligned</span> <span class="con">Risky if fair usage restriction is not placed on</span><br><span class="con">Upsell dependent on wider adoption</span></div>
      <div class="cell list stack"><span class="con">Not tightly value aligned (value may not increase linearly with usage)</span><span class="con">Not ARR</span></div>
      <div class="cell list stack"><span class="con">Delayed revenue realization</span><span class="con">Not ARR</span><span class="con">Tough to find the right metric</span></div>
      <div class="cell list list--nowrap"><span class="con">Limit on the number of tiers</span></div>
    </div>
  </section>

  <div class="brand-tab">
    <div class="brand-pill"><i></i>Strelquin</div>
  </div>
</body>
</html>
```